Business Cards and Stationary for Physio
Brookvale Phsyiotherapy Clinic
Business Cards and Stationary for Physio -
Creative Brief
Simple
First Last
Physiotherapist B. Physio
Street Name, City, Zip
info@brookvalephysiotherapy.example
www.brookvalephysiotherapy.example
Brookvale Phsyiotherapy Clinic. Next Appointment Date Time

```html
<!DOCTYPE html>
<html lang="en">
<head>
<meta charset="utf-8">
<title>Brookvale Phsyiotherapy Clinic – Business Cards</title>
<link rel="stylesheet" href="https://fonts.googleapis.com/css2?family=Open+Sans:wght@400;600;700&display=swap">
<style>
  :root {
    --page: #ffffff;
    --card: #ffffff;
    --green: #8cc63f;
    --navy: #2b3590;
    --text-light: #ffffff;
    --shadow: rgba(0, 0, 0, 0.22);
  }
  * { margin: 0; padding: 0; box-sizing: border-box; }
  html, body {
    width: 1200px;
    height: 927px;
    overflow: hidden;
    background: var(--page);
    font-family: "Open Sans", Arial, sans-serif;
  }
  .canvas { position: relative; width: 1200px; height: 927px; }

  .card {
    position: absolute;
    width: 560px;
    height: 320px;
    border-radius: 20px;
    background: var(--card);
    overflow: hidden;
    box-shadow: 0 10px 28px var(--shadow);
  }
  .card svg.card-shapes { position: absolute; inset: 0; }

  .card--front { left: 90px; top: 110px; }
  .card--back { left: 550px; top: 500px; }

  .brand {
    position: absolute;
    display: flex;
    align-items: center;
    gap: 10px;
  }
  .brand__mark {
    width: 26px;
    height: 26px;
    border-radius: 50%;
    background: var(--green);
    flex: none;
  }
  .brand__name {
    color: var(--navy);
    font-weight: 600;
    font-size: 17px;
    line-height: 1.15;
    letter-spacing: 0.2px;
  }
  .card--front .brand { left: 30px; top: 26px; }
  .card--back .brand { left: 180px; top: 130px; }

  .contact {
    position: absolute;
    left: 30px;
    top: 168px;
    color: var(--text-light);
  }
  .contact__name {
    font-weight: 700;
    font-size: 27px;
    line-height: 1.05;
  }
  .contact__title {
    font-size: 11px;
    margin-bottom: 12px;
  }
  .contact__line {
    font-size: 13px;
    line-height: 1.42;
  }
</style>
</head>
<body>
<main class="canvas">

  <section class="card card--front" aria-label="Business card front">
    <svg class="card-shapes" viewBox="0 0 560 320" width="560" height="320" aria-hidden="true">
      <path fill="var(--navy)" d="M0 98 C160 52 345 105 455 222 C492 262 514 296 526 320 L512 320 C500 298 480 268 442 230 C332 120 155 72 0 112 Z"/>
      <path fill="var(--green)" d="M0 112 C155 72 332 120 442 230 C480 268 500 298 512 320 L0 320 Z"/>
    </svg>
    <div class="brand">
      <span class="brand__mark"></span>
      <span class="brand__name">Brookvale<br>Phsyiotherapy Clinic</span>
    </div>
    <div class="contact">
      <p class="contact__name">First Last</p>
      <p class="contact__title">Physiotherapist B. Physio</p>
      <p class="contact__line">Street Name, City, Zip</p>
      <p class="contact__line">Phone: 613-555-0142</p>
      <p class="contact__line">Email: info@brookvalephysiotherapy.example</p>
      <p class="contact__line">Web address: www.brookvalephysiotherapy.example</p>
    </div>
  </section>

  <section class="card card--back" aria-label="Business card back">
    <svg class="card-shapes" viewBox="0 0 560 320" width="560" height="320" aria-hidden="true">
      <path fill="var(--navy)" d="M0 40 C18 150 40 250 70 320 L0 320 Z"/>
    </svg>
    <div class="brand">
      <span class="brand__mark"></span>
      <span class="brand__name">Brookvale<br>Phsyiotherapy Clinic</span>
    </div>
  </section>

</main>
</body>
</html>
```